Large Financial Advisory Firm Needs a Brochure!

We are looking for a modern and professional 4 page brochure for our Financial Advisory firm, Harbrook Counsel Group. I've attached multiple files to help with the completion of the design.
SIZE OF BROCHURE: 17 x 11 FLAT, 8.5 x 11 inch FOLDED
1. A PDF titled Design Brief will provide you with an overview of the project, the text to be included in the brochure and other misc. instructions.
2. Logo Files, you will need to incorporate our logo into the brochure design, I've attached all the files please select the images that suit your design.
3. Competitor Illustration - I've attached an image that needs to be included on the 2nd page (inside left cover of the brochure). You will need to incorporate the pros/cons of using our competitors and the advantages of using our firm. This is outlined in the Design Brief PDF.
NOTE: If possible please get rid of the blue sky in the illustration. Just use the buildings, the blue throws off the concept. I contacted the illustrator and am waiting for a design without the sky but it may not be ready in time so please delete it if possible.
- I like the Avenir fonts, 85 Heavy, 65 Medium and 45.

```html
<!DOCTYPE html>
<html lang="en">
<head>
<meta charset="utf-8">
<title>Harbrook Counsel Group – Brochure Spread</title>
<link rel="stylesheet" href="https://fonts.googleapis.com/css2?family=Nunito+Sans:wght@400;600;800&display=swap">
<style>
  :root {
    --backdrop: #e6e6e7;
    --charcoal: #48484b;
    --charcoal-deep: #3a3a3d;
    --ink: #3b3b3e;
    --ink-soft: #5a5a5e;
    --gold: #f2b51e;
    --amber: #f7c948;
    --ember: #e2692a;
    --paper: #f7f6f4;
    --white: #ffffff;
  }
  * { box-sizing: border-box; margin: 0; padding: 0; }
  html, body { width: 1200px; height: 683px; overflow: hidden; }
  body {
    background: var(--backdrop);
    font-family: "Nunito Sans", "Avenir", sans-serif;
    color: var(--ink);
  }
  .spread {
    position: absolute;
    left: 100px; top: 18px;
    width: 1000px; height: 646px;
    display: flex;
    box-shadow: 0 6px 22px rgba(0,0,0,.18);
  }
  .page {
    position: relative;
    width: 500px; height: 646px;
    overflow: hidden;
    background: var(--paper);
  }
  .page-back { border-right: 1px solid rgba(0,0,0,.08); }

  .photo-wash {
    position: absolute; inset: 0;
  }
  .page-back .photo-wash {
    background:
      radial-gradient(ellipse at 70% 30%, rgba(200,190,175,.45), transparent 60%),
      linear-gradient(160deg, #f4f2ee 0%, #e9e5df 45%, #efece7 100%);
  }
  .page-front .photo-wash {
    background:
      radial-gradient(ellipse 38% 30% at 58% 22%, #d9b9a3 0%, rgba(217,185,163,0) 100%),
      radial-gradient(ellipse 45% 45% at 62% 62%, #f4f4f6 0%, rgba(244,244,246,0) 100%),
      linear-gradient(120deg, #6d655d 0%, #a79c8f 35%, #c9c2b8 60%, #8d8378 100%);
  }

  .shapes { position: absolute; inset: 0; }

  .brand {
    position: absolute;
    display: flex; align-items: center; gap: 7px;
  }
  .brand-mark { width: 16px; height: 16px; }
  .brand-name {
    font-weight: 800;
    font-size: 11px;
    line-height: 1.05;
    letter-spacing: .08em;
    text-transform: uppercase;
  }
  .page-back .brand { left: 34px; top: 34px; }
  .page-back .brand-mark { background: var(--charcoal); }
  .page-back .brand-name { color: var(--charcoal); }
  .page-front .brand { right: 30px; bottom: 30px; }
  .page-front .brand-mark { background: var(--white); width: 22px; height: 22px; }
  .page-front .brand-name { color: var(--white); font-size: 15px; }

  .team {
    position: absolute;
    left: 34px; top: 74px; width: 432px;
  }
  .team-title {
    font-weight: 800;
    font-size: 30px;
    color: var(--ink-soft);
    margin-bottom: 10px;
  }
  .bio { margin-bottom: 8px; font-size: 8px; line-height: 1.45; color: var(--ink); }
  .bio-name { font-weight: 600; }
  .bio-role { font-weight: 600; color: var(--ink-soft); }

  .contact {
    position: absolute;
    left: 120px; top: 500px;
    color: var(--white);
  }
  .contact-title { font-weight: 600; font-size: 20px; margin-bottom: 4px; }
  .contact-line { font-size: 12px; line-height: 1.45; opacity: .92; }
</style>
</head>
<body>
<main class="spread">

  <section class="page page-back">
    <div class="photo-wash" role="img" aria-label="Faded, blurred office interior photograph behind the team text"></div>
    <svg class="shapes" viewBox="0 0 500 646" width="500" height="646" aria-hidden="true">
      <path d="M330,0 C400,14 455,28 500,46 L500,0 Z" fill="var(--charcoal)"/>
      <path d="M300,0 C385,16 450,34 500,58" fill="none" stroke="var(--gold)" stroke-width="4"/>
      <path d="M0,478 C150,450 330,440 500,382 L500,646 L0,646 Z" fill="var(--charcoal)"/>
      <path d="M0,466 C150,438 330,428 500,370" fill="none" stroke="var(--gold)" stroke-width="5"/>
      <path d="M0,474 C150,446 330,436 500,378" fill="none" stroke="var(--amber)" stroke-width="1.5" opacity=".7"/>
    </svg>

    <div class="brand">
      <span class="brand-mark"></span>
      <span class="brand-name">Harbrook<br>Counsel Group</span>
    </div>

    <article class="team">
      <h1 class="team-title">Our Team</h1>
      <p class="bio"><span class="bio-name">Daniel Morrow, CPA, CFA</span><br><span class="bio-role">Founder</span><br>
        Daniel works closely with advisors to build lasting succession plans. He brings creative thinking and deep experience to an industry in need of fresh ideas. Before founding the firm, he served as a regional director at a national advisory network, where he guided dozens of practices through growth, mergers and transitions. Daniel holds a degree in accounting and finance and enjoys travel, languages and cycling.</p>
      <p class="bio"><span class="bio-name">Owen Pryce</span><br><span class="bio-role">Partner</span><br>
        Owen has over ten years of experience in the financial services industry. He has served as a portfolio manager and research analyst, and today leads deal structure and operations for the firm. Owen grew up in the Pacific Northwest, studied economics, and holds the Chartered Financial Analyst designation. He lives with his wife and two children and enjoys hiking, cooking and reading.</p>
      <p class="bio"><span class="bio-name">Miles Carver</span><br><span class="bio-role">Founder</span><br>
        Miles brings over ten years of M&amp;A experience to the group. His expertise covers deal structure, management and corporate finance, allowing him to design custom succession plans for advisors. He earned a degree in economics and communications. Miles and his wife have four active young children, and he enjoys triathlons, travel and time with family.</p>
    </article>

    <address class="contact" style="font-style:normal">
      <h2 class="contact-title">Contact Us</h2>
      <p class="contact-line">Founder,</p>
      <p class="contact-line">Daniel Morrow,</p>
      <p class="contact-line">Phone: 555-014-2276</p>
      <p class="contact-line">daniel.morrow@harbrookcg.com</p>
    </address>
  </section>

  <section class="page page-front">
    <div class="photo-wash" role="img" aria-label="Portrait photograph of the firm's founder in a white shirt and dark tie, seated in an office"></div>
    <svg class="shapes" viewBox="0 0 500 646" width="500" height="646" aria-hidden="true">
      <path d="M0,0 L190,0 C130,22 70,36 0,52 Z" fill="var(--charcoal)"/>
      <path d="M0,62 C75,46 140,30 215,0" fill="none" stroke="var(--gold)" stroke-width="4"/>
      <path d="M0,646 L0,612 C170,618 360,570 500,468 L500,646 Z" fill="var(--charcoal-deep)"/>
      <path d="M0,600 C170,606 360,558 500,456" fill="none" stroke="var(--ember)" stroke-width="6"/>
    </svg>
    <div class="brand">
      <span class="brand-mark"></span>
      <span class="brand-name">Harbrook<br>Counsel Group</span>
    </div>
  </section>

</main>
</body>
</html>
```